Website Redesign project for agency

we're looking to see some new designs for an agency website.
details in this google doc: https://files.brindlepath.example/sheet/d/7QXvRk2PaLw9HsNe4TyUc8JbZoMf3Gd61572-qKrA9w/view?mode=shared
homepage and one inner page/ or the blog page
please visit the google doc above to see the website that needs to be redesigned as well as an example website we like.
if you have any questions please send them to us asap
thank you
Target Market(s)
small business owners
Number of Pages Required
2 page
Font styles to use
Sans Serif
Requirements
Nice to have
- custom design
Should not have
- do not use a template you find online

```html
<!DOCTYPE html>
<html lang="en">
<head>
<meta charset="utf-8">
<title>Northbeam Studio — Homepage</title>
<link href="https://fonts.googleapis.com/css2?family=Work+Sans:wght@500;600;700;800&family=Roboto:wght@400;500;700&display=swap" rel="stylesheet">
<style>
:root{
  --ink:#2b2d2f;
  --muted:#5a5d61;
  --dark:#2f3436;
  --purple:#4a2fd9;
  --purple-soft:#6d5ff6;
  --green:#5cb646;
  --gray:#f2f2f2;
  --white:#ffffff;
}
*{box-sizing:border-box;margin:0;padding:0}
html,body{width:1200px;height:1200px;overflow:hidden;background:var(--white)}
body{font-family:"Roboto",Arial,sans-serif;color:var(--ink)}
.stage{position:absolute;left:0;top:0;width:1932px;height:1932px;transform:scale(.62112);transform-origin:0 0;background:var(--white)}
.page{position:absolute;left:718px;top:0;width:496px;height:1932px;overflow:hidden}
.abs{position:absolute}
.band{position:absolute;left:0;width:496px}
.title{font-family:"Work Sans",Arial,sans-serif;font-weight:800;font-size:19.5px;line-height:22px;text-align:center;width:496px;left:0;letter-spacing:.3px}
.rule{position:absolute;width:22px;height:2px;background:var(--purple);left:237px}
.btn{position:absolute;height:16px;font-size:5.4px;letter-spacing:.5px;text-transform:uppercase;display:flex;align-items:center;justify-content:center;font-family:"Roboto",sans-serif;font-weight:500}
.btn-green{background:var(--green);color:var(--white)}
.btn-outline{border:1px solid var(--white);color:var(--white)}
.copy{font-size:5.2px;line-height:8.7px;color:var(--muted)}
.brand{font-family:"Work Sans",sans-serif;font-weight:700;color:var(--white);font-size:9px;letter-spacing:.3px;display:flex;align-items:center;gap:4px}
.brand i{display:block;width:6px;height:6px;border-radius:50%;background:var(--white)}
.topbar{top:0;height:14px;background:var(--dark);color:#cfd2d4;font-size:5px}
.nav{top:14px;height:28px;background:var(--purple)}
.nav-links{position:absolute;right:104px;top:11px;display:flex;gap:10px;font-size:5.3px;color:var(--white)}
.hero{top:42px;height:237px;background:linear-gradient(180deg,#6b6f73 0%,#4c4f52 45%,#2a2b2d 100%)}
.hero-title{position:absolute;left:0;width:496px;top:97px;text-align:center;color:var(--white);font-family:"Work Sans",sans-serif;font-weight:700;font-size:17.3px;line-height:19px}
.services{top:572px;height:281px;background:var(--gray)}
.svc{position:absolute;top:93px;width:124px;height:156px;text-align:center}
.svc h3{position:absolute;top:62px;width:100%;font-family:"Work Sans",sans-serif;font-weight:500;font-size:7.6px;color:var(--muted)}
.svc p{position:absolute;top:79px;left:20px;width:84px;font-size:5.2px;line-height:8.7px;color:var(--muted)}
.svc .btn{top:112px;left:30px;width:65px}
.svc-featured{background:var(--purple);border-radius:5px}
.svc-featured h3,.svc-featured p{color:var(--white)}
.agency{top:853px;height:207px;background:linear-gradient(120deg,#6e60f4,#7466f6 50%,#6a5cf2)}
.projects{top:1060px;height:437px;background:var(--white)}
.gallery{position:absolute;top:81px;left:0;width:496px;height:356px;background:#f8f8f8}
.shot{position:absolute;border:1px solid #c9cbd0}
.clients{top:1497px;height:271px;background:var(--purple)}
.quote{position:absolute;top:0;width:124px}
.avatar{position:absolute;top:73px;width:31px;height:31px;border-radius:50%;background:linear-gradient(#d9d4e8,#8c86a8);border:2px solid #ffffff}
.stars{position:absolute;top:114px;color:var(--green);font-size:9px;letter-spacing:1.5px}
.quote p{position:absolute;top:135px;left:0;width:124px;font-size:5.2px;line-height:8.7px;color:var(--white)}
.who{position:absolute;top:211px;font-size:5.2px;line-height:8.7px;color:var(--green)}
.who b{font-weight:500}
.footer{top:1768px;height:164px;background:var(--dark);color:#d8dadc}
.fcol{position:absolute;top:52px;font-size:5.2px;line-height:8.7px}
.fcol h4{font-family:"Work Sans",sans-serif;font-weight:500;font-size:7.4px;letter-spacing:.8px;color:var(--white);margin-bottom:9px}
.green{color:var(--green)}
</style>
</head>
<body>
<div class="stage">
<div class="page">

  <header class="band topbar">
    <div class="abs" style="left:51px;top:4px;display:flex;gap:6px;align-items:center">
      <svg width="6" height="5" viewBox="0 0 6 5"><rect x=".4" y=".4" width="5.2" height="4.2" fill="none" stroke="#cfd2d4" stroke-width=".7"/><path d="M.4.6 3 2.8 5.6.6" fill="none" stroke="#cfd2d4" stroke-width=".7"/></svg>
      <span>hello@northbeamstudio.example</span>
      <svg width="6" height="6" viewBox="0 0 6 6"><path d="M1.2.5 2.3 1.8 1.7 2.7Q2.5 4 3.4 4.4L4.2 3.8 5.5 4.8 4.8 5.6Q2.5 5.3.5 1.2Z" fill="none" stroke="#cfd2d4" stroke-width=".6"/></svg>
      <span>555-014-2290</span>
    </div>
    <div class="btn btn-green" style="left:397px;top:2px;width:49px;height:10px;font-size:4.6px">Client Portal</div>
  </header>

  <nav class="band nav">
    <div class="brand abs" style="left:51px;top:9px"><i></i>Northbeam Studio</div>
    <div class="nav-links"><span>Projects</span><span>Who We Are ▾</span><span>What We Do ▾</span><span>Book Us</span></div>
  </nav>

  <section class="band hero" role="img" aria-label="Photo of a smiling creative team standing together in a bright loft office">
    <div class="rule" style="top:88px"></div>
    <h1 class="hero-title">We Are A Web Design Company<br>Based In Boston, Ma</h1>
    <div class="btn btn-outline" style="left:193px;top:151px;width:61px;color:var(--green);border-color:var(--green)">See Our Work</div>
    <div class="btn btn-green" style="left:257px;top:151px;width:62px">Book Now!</div>
  </section>

  <section class="band" style="top:279px;height:293px">
    <div class="rule" style="top:21px"></div>
    <h2 class="title abs" style="top:36px">Who We Are</h2>
    <div class="abs" style="left:51px;top:82px;font-size:6.6px;font-weight:500;color:var(--muted)">Website Design, SEO or Social Media Marketing</div>
    <p class="copy abs" style="left:51px;top:104px;width:190px">Whether you need a new Website, SEO, Social Media or marketing plan, we're up for the task. Northbeam Studio has a team of talented developers, designers &amp; inbound marketers at your disposal. We'll help you own your local or national market within your industry.</p>
    <p class="copy abs" style="left:51px;top:148px;width:192px">We're the most reviewed and highest rated Web Design company in Boston that focuses on services that include inbound marketing, <span class="green">search engine optimization</span>, <span class="green">social media marketing</span>, lead conversion, to nurturing, and marketing automation. We perform high-end mobile-friendly web design, content creation, SEO, social media strategy development, email marketing, and more. Our clients in Boston and around the town enjoy more website visitors, more conversions, and best of all a better return on investment.</p>
    <div class="abs" role="img" aria-label="Illustration of a small team assembling a website layout" style="left:252px;top:66px;width:195px;height:150px;border-radius:6px;background:linear-gradient(135deg,#f1f0fb,#e4e1f8)"></div>
    <div class="btn btn-green" style="left:200px;top:233px;width:96px">Request A Free Quote</div>
  </section>

  <section class="band services">
    <div class="rule" style="top:30px;left:239px"></div>
    <h2 class="title abs" style="top:45px;left:2px">What We Do</h2>
    <div class="svc" style="left:50px">
      <svg class="abs" style="left:48px;top:28px" width="29" height="22" viewBox="0 0 29 22"><rect x="1" y="1" width="27" height="20" rx="2" fill="none" stroke="#5cb646" stroke-width="2"/><rect x="1" y="1" width="27" height="4" fill="#5cb646"/><rect x="4" y="8" width="13" height="4" fill="#5cb646"/><rect x="4" y="14" width="13" height="4" fill="#5cb646"/><rect x="19" y="8" width="6" height="10" fill="#5cb646"/></svg>
      <h3>Web Design</h3>
      <p>Web design to convert site visitors into customers.</p>
      <div class="btn btn-green" style="left:36px">Learn More</div>
    </div>
    <div class="svc svc-featured" style="left:186px">
      <svg class="abs" style="left:48px;top:27px" width="30" height="24" viewBox="0 0 30 24"><path d="M2 1V22H29" fill="none" stroke="#fff" stroke-width="3"/><path d="M7 17 13 10 17 14 25 6" fill="none" stroke="#fff" stroke-width="3"/><path d="M21 4H27V10" fill="none" stroke="#fff" stroke-width="3"/></svg>
      <h3>Search Engine Optimization</h3>
      <p>Search engine optimization for more traffic.</p>
      <div class="btn btn-outline">Learn More</div>
    </div>
    <div class="svc" style="left:342px">
      <svg class="abs" style="left:50px;top:28px" width="26" height="22" viewBox="0 0 26 22"><circle cx="13" cy="5" r="4" fill="#5cb646"/><circle cx="5" cy="8" r="3" fill="#5cb646"/><circle cx="21" cy="8" r="3" fill="#5cb646"/><path d="M6 21Q6 11 13 11Q20 11 20 21Z" fill="#5cb646"/><path d="M0 18Q0 12 5 12Q7 12 8 13Q5 15 5 18Z" fill="#5cb646"/><path d="M26 18Q26 12 21 12Q19 12 18 13Q21 15 21 18Z" fill="#5cb646"/></svg>
      <h3>Social Media Marketing</h3>
      <p>Engage in conversations with customers online.</p>
      <div class="btn btn-green" style="left:36px">Learn More</div>
    </div>
  </section>

  <section class="band agency" role="img" aria-label="Faded photo of a design team working at laptops, tinted violet">
    <h2 class="abs" style="left:0;width:486px;top:62px;text-align:center;font-family:'Work Sans',sans-serif;font-weight:700;font-size:14.6px;color:#fff">The Top Boston Web Design Agency</h2>
    <p class="copy abs" style="left:150px;top:90px;width:180px;color:#fff">All our custom websites are built with responsive design so they will look great on desktops, tablets, and mobile phones. Your customers will have no problem reaching you no matter what device they're on.</p>
    <div class="btn btn-green" style="left:218px;top:127px;width:61px">Book Now!</div>
  </section>

  <section class="band projects">
    <div class="rule" style="top:21px"></div>
    <h2 class="title abs" style="top:36px">Projects</h2>
    <p class="copy abs" style="left:138px;top:66px;width:226px;text-align:center">We do a lot more than just build awesome websites. We partner with all our clients to build relationships and create marketing plans that help them improve their business.</p>
    <div class="gallery">
      <div class="shot" role="img" aria-label="Screenshot of a medical billing client website on desktop and phone" style="left:52px;top:22px;width:194px;height:125px;background:linear-gradient(135deg,#c73a2a 0%,#1d6fb8 50%,#e8eaef 100%)"></div>
      <div class="shot" role="img" aria-label="Screenshot of a home builder client website" style="left:250px;top:22px;width:95px;height:125px;background:linear-gradient(180deg,#2d3b52 0%,#8aa0b8 30%,#f4f5f7 32%,#e5e8ec 100%)"></div>
      <div class="shot" role="img" aria-label="Screenshot of an interior renovation client website" style="left:348px;top:22px;width:95px;height:125px;background:linear-gradient(180deg,#2a2f38 0%,#4b5160 30%,#f4f5f7 32%,#d8dadf 100%)"></div>
      <div class="shot" role="img" aria-label="Screenshot of a golf course client website" style="left:52px;top:151px;width:95px;height:125px;background:linear-gradient(180deg,#3d5238 0%,#6e7d5e 28%,#f6f6f6 30%,#e9e9e9 94%,#222 95%)"></div>
      <div class="shot" role="img" aria-label="Music website project preview with violet overlay" style="left:151px;top:151px;width:194px;height:125px;background:linear-gradient(135deg,#6f5ff4,#7a6cf5);border-color:#7a6cf5">
        <div class="abs" style="left:14px;top:8px;font-family:'Work Sans',sans-serif;font-weight:500;font-size:12.5px;color:#fff;letter-spacing:.4px">Little Melodies!</div>
        <div class="abs" style="left:14px;top:24px;font-size:5.2px;letter-spacing:.7px;color:#fff">MUSIC WEBSITE DESIGN</div>
        <div class="abs" style="left:111px;top:109px;font-size:5.4px;letter-spacing:.7px;color:#fff;font-weight:500;display:flex;align-items:center;gap:5px">VIEW PROJECT <svg width="12" height="5" viewBox="0 0 12 5"><path d="M0 2.5H11M9 .5 11 2.5 9 4.5" fill="none" stroke="#fff" stroke-width=".8"/></svg></div>
      </div>
      <div class="shot" role="img" aria-label="Screenshot of a real estate client website" style="left:348px;top:151px;width:95px;height:125px;background:linear-gradient(180deg,#f5f6f8 0%,#6a7d92 12%,#9fb0c2 30%,#f5f6f8 32%,#eceef1 100%)"></div>
      <div class="btn btn-green" style="left:209px;top:295px;width:90px">See Our Portfolio</div>
    </div>
  </section>

  <section class="band clients">
    <div class="rule" style="top:23px;left:241px;background:var(--green)"></div>
    <h2 class="title abs" style="top:38px;left:4px;color:#fff">What Clients Say</h2>
    <div class="quote" style="left:51px">
      <div class="avatar" role="img" aria-label="Client portrait" style="left:46px"></div>
      <div class="stars" style="left:33px">★★★★★</div>
      <p>Dana and her team were incredibly responsive, resourceful, and diligent. Dana specifically translated "non-web savvy" ideas promoted by us, into a site that exceeded our expectations. We would recommend Northbeam Studio to anyone considering anything to do with website design, SEO, and marketing!</p>
      <div class="who"><b>Marcus Elden</b><br>Managing Member, Granite Ridge Partners</div>
    </div>
    <div class="quote" style="left:186px">
      <div class="avatar" role="img" aria-label="Client portrait" style="left:46px"></div>
      <div class="stars" style="left:33px">★★★★★</div>
      <p>Dana Whitlock at Northbeam Studio has been terrific to work with. Dana provided valuable direction and insight. If you are looking for creative talent and strategic direction, Northbeam Studio is a good place to start.</p>
      <div class="who"><b>Paul Kestrel</b><br>Founder &amp; CEO, Clearline Health Services</div>
    </div>
    <div class="quote" style="left:321px">
      <div class="avatar" role="img" aria-label="Client portrait" style="left:46px"></div>
      <div class="stars" style="left:33px">★★★★★</div>
      <p>Northbeam Studio just redesigned our nonprofit website and we couldn't be happier with the results. The team is very pleasing to work with, professional, responsive to our requests and always made sure that the product met our expectations. I would definitely recommend Northbeam Studio to anyone looking to create or redesign their website!</p>
      <div class="who"><b>Lucia M. Ortega-Vance, MD</b><br>Secretary &amp; Chief Operational Officer, Island Forward</div>
    </div>
  </section>

  <footer class="band footer">
    <div class="brand abs" style="left:51px;top:23px"><i></i>Northbeam Studio</div>
    <div class="fcol" style="left:51px"><h4>LOCATION</h4>Boston Website Design<br>18 Harbor Row #210,<br>Boston, MA 02110</div>
    <div class="fcol" style="left:152px"><h4>BUSINESS HOURS</h4>Monday - Saturday<br>8AM – 8PM</div>
    <div class="fcol" style="left:253px"><h4>CONTACT</h4><span class="green">hello@northbeamstudio.example</span><br>555-014-2290</div>
    <div class="fcol" style="left:355px"><h4>CONNECT</h4>
      <svg width="76" height="8" viewBox="0 0 76 8"><circle cx="4" cy="4" r="3.2" fill="#5cb646"/><circle cx="19" cy="4" r="3.2" fill="#5cb646"/><rect x="31" y="1" width="6" height="6" rx="1" fill="#5cb646"/><rect x="47" y="1" width="6" height="6" fill="#5cb646"/><rect x="64" y="1" width="9" height="6" rx="2" fill="#5cb646"/></svg>
    </div>
    <div class="abs" style="left:51px;top:116px;width:396px;height:1px;background:#454a4d"></div>
    <div class="abs" style="left:51px;top:133px;font-size:4.8px;line-height:8.7px"><span class="green">Privacy Policy</span> | <span class="green">Terms of Use</span><br>© 2021 Northbeam Studio. All Rights Reserved.</div>
  </footer>

</div>
</div>
</body>
</html>
```